Banner ad to encourage people to complete a survey

This is a banner ad which will be posted on www.veltrona.org. The goal of the add is to encourage people to click on it and take the survey.
File Format: Standard .jpg image (no Flash)
Ad dimension (Pixels): 300w x 250d
Max File Size: 24k
- Use a border to differentiate the banner from page content (page background is white)
- No transparent backgrounds
Ad Message: "Speech-Language Pathologist Survey"
Additional text: "Please take two minutes to complete a survey on the future of work patterns for Speech-Language Pathologists and enter a draw to win an Zorbik"
Target Market(s)
The respondents are professional and well educated and the ad/colour scheme should reflect this.
Font styles to use
Colors
Designer to choose colors to be used in the design.
Look and feel

```html
<!DOCTYPE html>
<html lang="en">
<head>
<meta charset="utf-8">
<title>Speech-Language Pathologist Survey – Banner</title>
<link rel="stylesheet" href="https://fonts.googleapis.com/css2?family=Raleway:wght@500;600;700&family=Open+Sans:wght@400;500&display=swap">
<style>
  :root {
    --stage-bg: #e8e5e1;
    --banner-purple: #7c5684;
    --header-white: #ffffff;
    --title-navy: #1f2b45;
    --stripe-blue: #3b5ba3;
    --stripe-red: #c4263d;
    --body-white: #ffffff;
    --button-slate: #2b3947;
    --art-light: #c9a0c9;
    --art-dark: #5a3a62;
  }
  html, body {
    margin: 0;
    padding: 0;
    width: 1200px;
    height: 710px;
    overflow: hidden;
    background: var(--stage-bg);
  }
  .canvas {
    position: relative;
    width: 1200px;
    height: 710px;
  }
  .banner {
    position: absolute;
    left: 210px;
    top: 30px;
    width: 300px;
    height: 250px;
    background: var(--banner-purple);
    transform: scale(2.6);
    transform-origin: 0 0;
    overflow: hidden;
  }
  .banner-header {
    position: absolute;
    left: 0;
    top: 6px;
    width: 265px;
    height: 70px;
    background: var(--header-white);
  }
  .banner-title {
    position: absolute;
    left: 15px;
    top: 11px;
    margin: 0;
    font-family: "Raleway", sans-serif;
    font-weight: 600;
    font-size: 20.5px;
    line-height: 25px;
    color: var(--title-navy);
    letter-spacing: -0.1px;
    white-space: nowrap;
  }
  .accent-stripe {
    position: absolute;
    top: 6px;
    width: 6px;
    height: 70px;
  }
  .accent-stripe--blue { left: 265px; background: var(--stripe-blue); }
  .accent-stripe--red { left: 271px; background: var(--stripe-red); }
  .banner-copy {
    position: absolute;
    left: 15px;
    top: 80px;
    margin: 0;
    font-family: "Open Sans", sans-serif;
    font-size: 14px;
    line-height: 16.5px;
    color: var(--body-white);
    white-space: nowrap;
  }
  .survey-art {
    position: absolute;
    left: 176px;
    top: 100px;
    width: 118px;
    height: 90px;
    border-radius: 8px;
    background: linear-gradient(150deg, var(--art-light), var(--art-dark));
  }
  .cta-button {
    position: absolute;
    left: 19px;
    top: 196px;
    width: 267px;
    height: 43px;
    border-radius: 4px;
    background: var(--button-slate);
    display: flex;
    align-items: center;
    justify-content: center;
    text-align: center;
    font-family: "Raleway", sans-serif;
    font-weight: 600;
    font-size: 12.5px;
    line-height: 17px;
    letter-spacing: 0.6px;
    color: var(--body-white);
    text-transform: uppercase;
    text-decoration: none;
  }
</style>
</head>
<body>
  <main class="canvas">
    <section class="banner" aria-label="Speech-Language Pathologist Survey banner">
      <div class="banner-header">
        <h1 class="banner-title">Speech-Language<br>Pathologist Survey</h1>
      </div>
      <span class="accent-stripe accent-stripe--blue"></span>
      <span class="accent-stripe accent-stripe--red"></span>
      <p class="banner-copy">Please take two minutes to<br>complete a survey on<br>the future of work<br>patterns for<br>Speech-Language<br>Pathologists</p>
      <div class="survey-art" role="img" aria-label="Illustration of two hands holding a tablet showing a survey checklist"></div>
      <a class="cta-button" href="#">Take the survey now&nbsp; and<br>enter a draw to win an Zorbik</a>
    </section>
  </main>
</body>
</html>
```